Unternehmen für Ordnung und Sauberkeit am Arbeitsplatz und Produkte zur Produktionsoptimierung benötigt Visitenkarten und Briefpapier
Zielgruppe
Produkte für Ordnung und Sauberkeit am Arbeitsplatz, Organisation von Arbeitsplätzen, Produkte zur Vereinfachung von Arbeitsabläufen, Produkte zur Produktionsoptimierung unter dem Lean Gedanke, Schlagwort: "5S", nachhaltig, sauber
Aufgabenstellung
Wir sind auf der Suche nach Visitenkarten und Briefpapier für das Unternehmen taVork. Nachhaltig, Sauber usw.. Unser Firmenlogo finden Sie anbei.

```html
<!DOCTYPE html>
<html lang="de">
<head>
<meta charset="utf-8">
<title>taVork – Visitenkarte</title>
<link rel="stylesheet" href="https://fonts.googleapis.com/css2?family=Fira+Sans+Condensed:wght@400;600;700&display=swap">
<style>
  :root {
    --bg: #a9a9a9;
    --card: #ffffff;
    --green: #1f8a3c;
    --grey: #5f5f62;
    --ink: #1c1c1c;
    --mark: #4a4a4d;
  }
  * { box-sizing: border-box; margin: 0; padding: 0; }
  html, body {
    width: 1163px; height: 1200px; overflow: hidden;
    background: var(--bg);
    font-family: "Fira Sans Condensed", "Arial Narrow", sans-serif;
    color: var(--ink);
  }
  .card {
    position: absolute; left: 205px; width: 700px; height: 402px;
    background: var(--card); overflow: hidden;
  }
  .card--front { top: 196px; }
  .card--back  { top: 655px; }

  .brand { position: absolute; display: flex; align-items: center; }
  .brand__square { background: var(--green); border-radius: 6px; }
  .brand__name { font-weight: 700; color: var(--mark); letter-spacing: -0.5px; }

  .card--front .brand { left: 455px; top: 70px; gap: 12px; }
  .card--front .brand__square { width: 44px; height: 44px; }
  .card--front .brand__name { font-size: 48px; line-height: 1; }

  .card--back .brand { left: 218px; top: 176px; gap: 18px; }
  .card--back .brand__square { width: 60px; height: 60px; border-radius: 8px; }
  .card--back .brand__name { font-size: 66px; line-height: 1; }

  .person { position: absolute; left: 44px; top: 193px; }
  .person__name { font-size: 22px; font-weight: 700; line-height: 26px; }
  .person__role { font-size: 16px; margin-top: 8px; padding-left: 4px; }

  .name-rule {
    position: absolute; left: 253px; right: 0; top: 205px;
    height: 4px; background: var(--green);
  }

  .contact { position: absolute; font-size: 17px; line-height: 22px; white-space: nowrap; }
  .contact--address { left: 49px; top: 284px; }
  .contact--web     { left: 257px; top: 302px; }
  .contact--phone   { left: 479px; top: 302px; }

  .band { position: absolute; left: 0; bottom: 0; width: 700px; height: 22px; display: block; }
</style>
</head>
<body>
  <section class="card card--front">
    <div class="brand">
      <span class="brand__square"></span>
      <span class="brand__name">taVork</span>
    </div>

    <div class="person">
      <p class="person__name">Jonas Feldmann</p>
      <p class="person__role">Geschäftsführer</p>
    </div>
    <div class="name-rule"></div>

    <p class="contact contact--address">Lindenweg 12<br>79100 Talheim<br>Germany</p>
    <p class="contact contact--web">mail: info@tavork.de<br>www.tavork.de</p>
    <p class="contact contact--phone">tel: 0 12 34 / 56 78 90<br>fax: 0 12 34 / 56 78 91</p>

    <svg class="band" viewBox="0 0 700 22" aria-hidden="true">
      <polygon points="0,0 506,0 494,22 0,22" fill="var(--grey)"/>
      <polygon points="522,3 700,3 700,22 510,22" fill="var(--green)"/>
    </svg>
  </section>

  <section class="card card--back">
    <div class="brand">
      <span class="brand__square"></span>
      <span class="brand__name">taVork</span>
    </div>

    <svg class="band" viewBox="0 0 700 22" aria-hidden="true">
      <polygon points="0,0 515,0 503,22 0,22" fill="var(--green)"/>
      <polygon points="530,0 700,0 700,22 518,22" fill="var(--grey)"/>
    </svg>
  </section>
</body>
</html>
```